Upmarket building and construction company needs signage

Our building company R Brent Construction, needs signage to put up on the side of our vehicle trailers and on site fencing. We are a building company that specialises in residential construction and carpentry .

I will attach our logo and some inspirational pics for site fencing as well as what our trailer looks like .
Other details i would like on the sign are our
( email) rbrentconstruction@mailbox-example.net
(mobile ) 0493 518 264
(website ) rbrentconstruction. example.net

Target Market(s)

Home owners looking for a reliable local builder who produces good quality work. I have attached some inspirational pics.

Industry/Entity Type

Building and Construction

Colors

Designer to choose colors to be used in the design.

Requirements
Must have
• Our logo, contact information
Nice to have
• We would like the design to have elements of being Elegant, Serious, Modern, Professional, Masculine, Conservative and Upmarket.

```html
<!DOCTYPE html>
<html lang="en">
<head>
<meta charset="utf-8">
<title>R Brent Construction – Site Signage</title>
<link href="https://fonts.googleapis.com/css2?family=Oswald:wght@300;400;500&display=swap" rel="stylesheet">
<style>
  :root {
    --backdrop: #545454;
    --sign-white: #ffffff;
    --brand-grey: #6e6e6e;
    --band-grey: #777777;
    --frame-grey: #6b6b6b;
    --text-light: #ffffff;
  }
  html, body {
    margin: 0;
    padding: 0;
    width: 1199px;
    height: 1200px;
    overflow: hidden;
    background: var(--backdrop);
  }
  .canvas {
    position: relative;
    width: 1199px;
    height: 1200px;
    font-family: "Oswald", "Arial Narrow", sans-serif;
  }
  .sign {
    position: absolute;
    left: 210px;
    top: 81px;
    width: 777px;
    height: 1037px;
    background: var(--sign-white);
    overflow: hidden;
  }
  .brand {
    position: absolute;
    left: 0;
    right: 0;
    top: 150px;
    margin: 0;
    text-align: center;
    font-weight: 300;
    color: var(--brand-grey);
    line-height: 1;
  }
  .brand-name {
    display: block;
    font-size: 104px;
    letter-spacing: 6px;
  }
  .brand-line {
    display: block;
    margin-top: 14px;
    font-size: 46px;
    letter-spacing: 9px;
  }
  .services-frame {
    position: absolute;
    left: 46px;
    top: 495px;
    width: 685px;
    height: 227px;
    box-sizing: border-box;
    border: 3px solid var(--frame-grey);
  }
  .services-panel {
    position: absolute;
    left: 26px;
    top: 24px;
    width: 627px;
    height: 173px;
    background: var(--band-grey);
    display: flex;
    flex-direction: column;
    justify-content: center;
    align-items: center;
  }
  .services-line {
    margin: 0;
    color: var(--text-light);
    font-weight: 300;
    font-size: 50px;
    line-height: 64px;
    letter-spacing: 0.3px;
  }
  .contact-band {
    position: absolute;
    left: 0;
    bottom: 0;
    width: 100%;
    height: 236px;
    background: var(--band-grey);
    text-align: center;
    color: var(--text-light);
  }
  .contact-phone {
    position: absolute;
    left: 0;
    right: 0;
    top: 30px;
    margin: 0;
    font-weight: 500;
    font-size: 82px;
    line-height: 1.1;
  }
  .contact-email {
    position: absolute;
    left: 0;
    right: 0;
    top: 140px;
    margin: 0;
    font-weight: 400;
    font-size: 38px;
    line-height: 1.2;
  }
</style>
</head>
<body>
  <main class="canvas">
    <section class="sign">
      <h1 class="brand">
        <span class="brand-name">R BRENT</span>
        <span class="brand-line">CONSTRUCTION</span>
      </h1>

      <div class="services-frame">
        <div class="services-panel">
          <p class="services-line">NEW BUILDS | RENOVATIONS</p>
          <p class="services-line">RESIDENTATIAL | COMMERCIAL</p>
        </div>
      </div>

      <footer class="contact-band">
        <p class="contact-phone">+61 493 518 264</p>
        <p class="contact-email">rbrentconstruction@mailbox-example.net</p>
      </footer>
    </section>
  </main>
</body>
</html>
```